Wren Vehicle Polishing (Mobile detail)

I need a business card made up. I'd like it to be different in some form, either raised, embossed, debossed, something cool that stands out. (preferably embossed text somewhere in it). I will be including the Initial png file. Let me know if you need the photoshop of adobe illustrator file to work with.

Information to be included: Text: XXX-XXX-XXXX Phone: XXX-XXX-XXXX Email: wrenpolishcrew@mailbox-demo.net Website: www.socialpage-demo.net/wrenpolishKTR Hours of operation: Mon - Fri 7:00AM to 8:00PM Sat - 10:00AM to 8:00PM

Target Market(s)

Mobile automotive detailing

Industry/Entity Type

Automotive

Contact Information for Business Card

Make it stand out with embossed lettering, I'd also like the background to be glossy black or matte, something that represents a shiny car, black preferred

Requirements
Must have
• A glossy background, or something.
• My logo, pick one of them that best fits your design.
Should not have
• White background,
• something that does not stand out.

```html
<!DOCTYPE html>
<html lang="en">
<head>
<meta charset="utf-8">
<title>Wren Vehicle Polishing – Business Card</title>
<link rel="stylesheet" href="https://fonts.googleapis.com/css2?family=Varela+Round&display=swap">
<style>
  :root {
    --card-black: #0c0c0c;
    --card-charcoal: #2a2a2a;
    --card-sheen: #3d3d3d;
    --text-white: #ffffff;
    --mark-silver: #c9c9c9;
    --mark-accent: #e8642a;
    --ghost: rgba(255, 255, 255, 0.07);
  }
  html, body {
    margin: 0;
    padding: 0;
    width: 1200px;
    height: 686px;
    overflow: hidden;
    background: var(--card-black);
  }
  .card {
    position: relative;
    width: 1200px;
    height: 686px;
    overflow: hidden;
    font-family: "Varela Round", sans-serif;
    color: var(--text-white);
    background:
      radial-gradient(ellipse 70% 60% at 30% 18%, var(--card-sheen) 0%, transparent 70%),
      linear-gradient(100deg, var(--card-black) 0%, var(--card-charcoal) 35%, #141414 60%, var(--card-charcoal) 80%, var(--card-black) 100%);
  }
  .ghost-name {
    position: absolute;
    left: 40px;
    bottom: 30px;
    margin: 0;
    font-size: 92px;
    line-height: 1;
    color: var(--ghost);
    white-space: nowrap;
  }
  .brand {
    position: absolute;
    left: 66px;
    top: 70px;
    width: 370px;
    display: flex;
    align-items: center;
    gap: 20px;
  }
  .brand-dot {
    flex: none;
    width: 84px;
    height: 84px;
    border-radius: 50%;
    background: var(--mark-accent);
  }
  .brand-name {
    margin: 0;
    font-size: 44px;
    line-height: 1.08;
    color: var(--mark-silver);
  }
  .contact-main {
    position: absolute;
    left: 610px;
    top: 175px;
    width: 560px;
    text-align: center;
  }
  .person {
    margin: 0;
    font-size: 58px;
    line-height: 1.1;
  }
  .phone {
    margin: 4px 0 0;
    font-size: 62px;
    line-height: 1.1;
    letter-spacing: 1px;
  }
  .details {
    position: absolute;
    right: 38px;
    top: 500px;
    margin: 0;
    padding: 0;
    list-style: none;
    text-align: right;
    font-size: 27px;
    line-height: 39px;
  }
</style>
</head>
<body>
  <main class="card">
    <p class="ghost-name" aria-hidden="true">Wren Vehicle Polishing</p>

    <div class="brand">
      <span class="brand-dot" aria-hidden="true"></span>
      <p class="brand-name">Wren Vehicle Polishing</p>
    </div>

    <div class="contact-main">
      <p class="person">Milo Tanner</p>
      <p class="phone">321-555-014-208</p>
    </div>

    <ul class="details">
      <li class="email">wrenpolishcrew@mailbox-demo.net</li>
      <li class="web">www.socialpage-demo.net/wrenpolishKTR</li>
      <li class="hours">Mon - Fri 7:00AM to 8:00PM</li>
      <li class="hours">Sat - 10:00AM to 8:00PM</li>
    </ul>
  </main>
</body>
</html>
```